依頼詳細
小学4年生~中学3年生までのお子様を持つ親御様を対象とした
親子で学ぶ投資セミナーの広告になります。

広告先はLPです。

セミナーの内容は、親御さんがお子さんと一緒にオンヌカロセミナーで投資のやり方等投資の導入部分を学んでいただく内容となっております。

・イメージ
親子
楽しい
将来
役に立つ
未来
明るい

バナーにいれる内容はLPを見て考えていただきたいです。

記載項目
LPを見てキャッチコピーを考えてください。
サイズ
• 概要に載せてます
希望イメージ
シンプル 複雑
単色 カラフル
暗い 明るい
日常 高級
遊び心 厳粛
未来的 伝統的
女性的 男性的
希望する色
黄・オレンジ系、青系、水色系
納品ファイル
• 高解像度JPG (.jpg)
• イラストレーター形式 (.ai)
• フォトショップ形式 (.psd)
• PNG形式 (.png)
補足説明
写真でもイラストでも自由です。
判らないところがあればなんでも質問してください!

こちらの広告はまずはLPに飛んでもらってヌカロ登録をして頂くための広告になります。
ですので、将来のお金に対して不安を抱えている保護者や投資に興味があるけどよくわからない保護者に向けての広告になります。
■ 選んだ理由

ホームページのデザインにもマッチし、広告としてうまく使えそうなデザインでした。

■ 提案者全員のお礼・コメント

沢山のご提案ありがとうございました。
今後も機会がありましたらよろしくお願いします。

```html
<!DOCTYPE html>
<html lang="ja">
<head>
<meta charset="UTF-8">
<title>親子で学ぶマネースタディ</title>
<link rel="stylesheet" href="https://fonts.googleapis.com/css2?family=M+PLUS+Rounded+1c:wght@500;700;800;900&display=swap">
<style>
  :root {
    --page-bg: #eef2f6;
    --sky: #d8effb;
    --brand-blue: #1a86d6;
    --deep-navy: #1c2f6e;
    --accent-orange: #f08a12;
    --accent-red: #e2402c;
    --leaf-green: #3fae3a;
    --sun-yellow: #ffe14a;
    --white: #ffffff;
    --ink: #333b4a;
  }
  * { margin: 0; padding: 0; box-sizing: border-box; }
  html, body { width: 871px; height: 1200px; overflow: hidden; }
  body {
    background: var(--page-bg);
    font-family: "M PLUS Rounded 1c", sans-serif;
    color: var(--ink);
    position: relative;
  }
  .banner {
    position: absolute;
    left: 20px; top: 185px;
    width: 831px; height: 830px;
    background: var(--sky);
    overflow: hidden;
  }
  .headline-band {
    position: absolute; left: 0; top: 0; width: 100%; height: 74px;
    background: var(--brand-blue);
    display: flex; align-items: center; justify-content: center;
    color: var(--white); font-weight: 900; font-size: 44px; letter-spacing: 1px;
    white-space: nowrap;
  }
  .content-panel {
    position: absolute; left: 22px; top: 90px; width: 787px; height: 630px;
    background: var(--white);
    border: 4px solid var(--brand-blue);
    border-radius: 10px;
    overflow: hidden;
  }
  .lead {
    position: absolute; left: 0; top: 12px; width: 100%;
    text-align: center; font-weight: 900; font-size: 56px; line-height: 1.2;
    color: var(--brand-blue); white-space: nowrap;
  }
  .title {
    position: absolute; left: 0; top: 88px; width: 100%;
    text-align: center; font-weight: 900; font-size: 80px; line-height: 1.2;
    color: var(--deep-navy); white-space: nowrap;
  }
  .title .hl { color: var(--accent-red); }
  .level {
    position: absolute; right: 40px; top: 196px;
    font-size: 26px; font-weight: 800; color: var(--deep-navy); white-space: nowrap;
  }
  .illust { position: absolute; border-radius: 18px; }
  .illust.kids {
    left: 24px; top: 240px; width: 270px; height: 220px;
    background: radial-gradient(circle at 45% 50%, #ffd79a, #9fd3f2 80%);
  }
  .illust.teacher {
    left: 500px; top: 240px; width: 260px; height: 220px;
    background: radial-gradient(circle at 55% 55%, #f4c9a0, #c9e6f7 80%);
  }
  .question-bubble {
    position: absolute; left: 290px; top: 236px; width: 200px; height: 130px;
    background: var(--white); border: 4px solid var(--deep-navy); border-radius: 50%;
    display: flex; align-items: center; justify-content: center;
    text-align: center; line-height: 1.25;
    font-weight: 900; font-size: 30px; color: var(--deep-navy); white-space: nowrap;
  }
  .teacher-line {
    position: absolute; left: 0; top: 474px; width: 100%;
    display: flex; align-items: center; justify-content: center; gap: 14px;
    font-weight: 800; font-size: 28px; color: var(--brand-blue); white-space: nowrap;
  }
  .teacher-line .rule { width: 40px; height: 4px; background: var(--brand-blue); }
  .program-name {
    position: absolute; left: 0; top: 522px; width: 100%;
    text-align: center; font-weight: 900; font-size: 60px; line-height: 1.2;
    color: var(--accent-orange); white-space: nowrap;
  }
  .program-name .blue { color: var(--brand-blue); }
  .organizer {
    position: absolute; left: 0; top: 730px; width: 100%;
    text-align: center; font-weight: 700; font-size: 24px; color: var(--deep-navy);
    white-space: nowrap;
  }
  .audience-band {
    position: absolute; left: 0; bottom: 0; width: 100%; height: 62px;
    background: var(--brand-blue);
    display: flex; align-items: center; justify-content: center; gap: 12px;
    color: var(--white); font-weight: 800; font-size: 30px; white-space: nowrap;
  }
  .grade {
    background: var(--leaf-green); color: var(--sun-yellow);
    padding: 2px 14px; border-radius: 6px; font-weight: 900;
  }
</style>
</head>
<body>
  <section class="banner">
    <div class="headline-band">お金に困らない子にそだてる！</div>

    <div class="content-panel">
      <p class="lead">学校では教えてくれない</p>
      <h1 class="title">お金と<span class="hl">投資</span>の授業</h1>
      <p class="level">初心者向け</p>

      <div class="illust kids" role="img" aria-label="投資に興味を持つ親子のイラスト"></div>
      <div class="illust teacher" role="img" aria-label="グラフやお金を背景に解説する先生のイラスト"></div>
      <div class="question-bubble">“投資”って<br>な～に？</div>

      <p class="teacher-line"><span class="rule"></span>歯科医師ひろパパが教える<span class="rule"></span></p>
      <h2 class="program-name">親子で学ぶ<span class="blue">マネースタディ</span></h2>
    </div>

    <p class="organizer">金融教育オンヌカロセミナー　主催：合同会社ソラノ</p>

    <div class="audience-band">
      <span class="grade">小4</span>～<span class="grade">中3</span>のお子様と親御様対象
    </div>
  </section>
</body>
</html>
```